Wine Shop Banners

Banner graphic/images required
Require banner images to match the present online wine shop.

www.kelterhaus-traube.de

The wine-shop presently has a very clean, simple design, lots of white space, which is very much the trend at the moment.

Requirements
Images or graphic design for present banners visible on the homepage

The colour and feeling of the banners must fit in with the present clean, simple design.

Work required
3 large slide-card/banners (can be more) and 3 smaller fixed banners below. Please view website to see present position of banners.

LARGE BANNERS x 3

Something special with white background within the banner space
White background on each slide-card. Small individual graphic image in the middle of the slide card. This could be either a simple element of wine:
ingredients, fruit (grape), bottle, cork, old bottle label etc. just displaying one item on each slide-card. Preferably with high quality graphic features.

Note:
We are trying the steer away from the classic stereotype wineshop design. The image/s should have a higher, individual graphic touch, which gives the design something different. Sometimes such artistic work is displayed in steampunk or even in nostalgic design, which leaves the viewer slightly memorized with the content.
To clarify: we are not looking for a full steampunk design but possibly certain elements of this will give you an idea what we mean. That is to say, the design can go slightly in this direction without going over the top. Something small but very eye-catching.

SMALLER BANNERS x 3

One idea is:
Showing a symbol e.g. - discount sign "%" against a white background but again with a high graphic quality.

Target Market(s)

People interested in purchasing wine.
Ages approx. 25 to 65

Industry/Entity Type

Shop

Requirements
Must have
• Something special with white background
• Small individual graphic image in the middle of the slide card.
Nice to have
• The image/s should have a higher, individual graphic touch, which gives the design something different. Something that leaves the viewer slightly memorized with the content.
Should not have
• Not the typical classical design that is often seen on wine shops.

```html
<!DOCTYPE html>
<html lang="en">
<head>
<meta charset="utf-8">
<title>Wine Shop Banners – Slide Cards</title>
<link rel="stylesheet" href="https://fonts.googleapis.com/css2?family=Noticia+Text:ital@1&display=swap">
<style>
  :root {
    --page-bg: #ffffff;
    --rule-green: #4f8a1f;
    --frame: #4a1a22;
    --label: #4a1a22;
    --headline: #1a1a1a;
    --wash-blue: #d9edf1;
    --wash-yellow: #fdfdea;
    --wash-pink: #fbe3f4;
    --grape-dark: #2a1a26;
    --grape-mid: #5a2a3a;
    --wine-red: #8e1b2c;
    --glass: #f1eded;
    --basket: #a0783d;
    --bottle: #1f2a1c;
  }
  * { box-sizing: border-box; margin: 0; padding: 0; }
  html, body { width: 1200px; height: 903px; overflow: hidden; background: var(--page-bg); }
  body { position: relative; font-family: "Noticia Text", Georgia, serif; }

  .rule { position: absolute; left: 0; width: 1200px; background: var(--rule-green); }
  .rule--top { top: 0; height: 5px; }
  .rule--bottom { top: 898px; height: 5px; }

  .backdrop { position: absolute; left: 0; top: 0; width: 1200px; height: 903px; }

  .slide-label {
    position: absolute; left: 201px;
    font-style: italic; font-size: 16px; color: var(--label);
  }

  .slide-card {
    position: absolute; left: 279px; width: 642px; height: 250px;
    border: 1px solid var(--frame); background: #fff; overflow: hidden;
  }
  .slide-card--one { top: 45px; }
  .slide-card--two { top: 309px; }
  .slide-card--three { top: 575px; }

  .headline {
    position: absolute; top: 88px;
    font-style: italic; font-weight: 400; font-size: 26px; line-height: 31px;
    color: var(--headline);
  }
  .slide-card--one .headline, .slide-card--three .headline { left: 38px; }
  .slide-card--two .headline { left: 303px; }

  .artwork { position: absolute; }
  .artwork--grapes {
    left: 350px; top: 0; width: 286px; height: 249px;
    background: radial-gradient(ellipse 55% 60% at 50% 35%, var(--grape-mid) 0%, var(--grape-dark) 55%, rgba(255,255,255,0) 75%);
  }
  .artwork--pour {
    left: 0; top: 0; width: 232px; height: 249px;
    background: linear-gradient(160deg, var(--bottle) 0%, var(--glass) 30%, #f6eeee 55%, var(--wine-red) 90%);
    border-radius: 0 0 40% 0;
  }
  .artwork--still-life {
    left: 325px; top: 3px; width: 316px; height: 245px;
    background: linear-gradient(90deg, rgba(255,255,255,0) 0%, var(--grape-mid) 18%, var(--basket) 42%, var(--bottle) 62%, var(--wine-red) 85%, rgba(255,255,255,0) 100%);
    border-radius: 40% 40% 6px 6px;
  }
</style>
</head>
<body>
  <svg class="backdrop" viewBox="0 0 1200 903" aria-hidden="true">
    <polygon points="0,787 0,885 182,885 135,808 20,808" fill="var(--wash-blue)"/>
    <polygon points="322,834 442,834 490,898 370,898" fill="var(--wash-yellow)"/>
    <polygon points="820,834 900,834 935,898 855,898" fill="var(--wash-yellow)"/>
    <defs>
      <linearGradient id="pinkWash" x1="0" x2="1" y1="0" y2="0">
        <stop offset="0" stop-color="#ffffff"/>
        <stop offset="1" stop-color="var(--wash-pink)"/>
      </linearGradient>
    </defs>
    <polygon points="890,855 1132,855 1132,898 870,898" fill="url(#pinkWash)"/>
  </svg>

  <div class="rule rule--top"></div>

  <span class="slide-label" style="top:160px">Slide 1</span>
  <section class="slide-card slide-card--one">
    <h2 class="headline">Surprise of Wine Gifts<br>for Someone Special</h2>
    <div class="artwork artwork--grapes" role="img" aria-label="Bunch of dark red grapes with dripping juice"></div>
  </section>

  <span class="slide-label" style="top:411px">Slide 2</span>
  <section class="slide-card slide-card--two">
    <div class="artwork artwork--pour" role="img" aria-label="Red wine pouring from a bottle into a glass"></div>
    <h2 class="headline">Surprise of Wine Gifts<br>for Someone Special</h2>
  </section>

  <span class="slide-label" style="top:697px">Slide 3</span>
  <section class="slide-card slide-card--three">
    <h2 class="headline">Surprise of Wine Gifts<br>for Someone Special</h2>
    <div class="artwork artwork--still-life" role="img" aria-label="Wicker basket with spilled grapes, a wine bottle and two glasses of red wine"></div>
  </section>

  <div class="rule rule--bottom"></div>
</body>
</html>
```